Webdesign für SEO-Agentur
Zielgruppe
Wir bieten kleinen und mittelständischen Unternehmen Suchmaschinenoptimierung zum fairen Preis mit Erfolgsgarantie an. Unsere Zielgruppe sind Unternehmer die bisher wenig oder gar keine Erfahrungen mit SEO hatten. Wir möchten Unternehmen dabei helfen ihren digitalen Auftritt sowie dessen Sichtbarkeit zu verbessern um neue Kunden zu finden.
Aufgabenstellung
- seriöses und modernes Design bei gleichzeitig ansprechender Gestaltung
- passend zum Namen möchten wir, dass die Website einen leichten wissenschaftlichen/chemischen Touch erhält. Beachten Sie daher unsere Skizze zur Schritt für Schritt Darstellung. Weitere kleine Hinweise in Richtung Chemie oder Wissenschaft können und sollen eingebaut werden.
- vorerst nur Landing-Page, daher keine Navigation nötig. Wir erwarten eine vollständige Desktop sowie Mobilversion in Ihrem Design.
- Einhaltung der vorgegebenen Inhalte
- keine langweiligen Standard-Designs, auch besondere Seiten können seriös sein
- Header ist für Portrait der Mitarbeiter reserviert und benötigt daher eine gewisse freie Fläche

```html
<!DOCTYPE html>
<html lang="de">
<head>
<meta charset="utf-8">
<title>Kovalent Studio – SEO Beratung</title>
<link href="https://fonts.googleapis.com/css2?family=Lato:ital,wght@0,300;0,400;0,700;1,300&display=swap" rel="stylesheet">
<style>
:root{
  --navy:#0b3a66;
  --navy-deep:#063a66;
  --red:#ee1848;
  --bg:#f6f6f6;
  --panel:#dcdcdc;
  --text:#666;
  --white:#fff;
}
*{box-sizing:border-box;margin:0;padding:0}
html,body{width:1200px;height:3042px;overflow:hidden}
body{font-family:'Lato',sans-serif;background:var(--white);position:relative;color:var(--text)}
.page{position:absolute;left:40px;top:0;width:1160px;height:3042px;background:var(--bg);border-left:1px solid #e4e4e4}
.abs{position:absolute}
.shapes{position:absolute;left:0;top:0;width:1200px;height:3042px}
.center{left:0;width:1200px;text-align:center}
.title{color:var(--navy);font-weight:700;font-size:32px;line-height:37px}
.lead{left:292px;width:616px;text-align:center;font-weight:300;font-size:14px;line-height:21.7px}
.molecule{left:578px;width:44px;height:44px}
.field{position:absolute;height:42px;width:370px;border-radius:21px;background:var(--white);box-shadow:0 2px 4px rgba(0,0,0,.08);font-style:italic;font-weight:300;font-size:13px;color:#aaa;padding:12px 17px}
.btn{position:absolute;left:512px;width:175px;height:43px;border-radius:22px;background:var(--red);color:var(--white);font-size:15px;font-weight:400;text-align:center;line-height:43px}
.step-title{left:455px;top:1220px;color:var(--red);font-size:21px;font-weight:400}
.step-text{left:455px;top:1251px;width:450px;font-size:14px;line-height:21.6px;font-weight:300}
.step-text b{font-weight:700;color:#333}
.card{position:absolute;top:1689px;width:291px;height:266px;background:var(--white);box-shadow:0 1px 5px rgba(0,0,0,.07);padding:30px 25px}
.card h3{color:var(--red);font-size:16px;font-weight:700;margin-bottom:14px}
.card p{font-size:12.5px;line-height:20px;font-weight:300}
.benefit{position:absolute;font-size:15px;line-height:21px}
.benefit strong{display:block;color:#333;font-weight:400}
.benefit span{font-weight:300}
.tick{position:absolute;width:28px;height:28px}
.contact{font-size:15px;line-height:22px;font-weight:300}
.footer{top:2999px;font-size:15px;font-weight:300}
</style>
</head>
<body>
<div class="page"></div>

<svg class="shapes" viewBox="0 0 1200 3042">
  <path d="M40 0 H213 Q222 40 200 80 L40 351 Z" fill="var(--red)"/>
  <path d="M180 437 L1200 531 V996 L210 909 Q180 906 175 870 L122 510 Q118 437 180 437 Z" fill="var(--panel)"/>
  <path d="M40 1291 L200 1420 Q240 1455 210 1505 L40 1792 Z" fill="var(--red)"/>
  <path d="M1200 1940 L1040 2070 Q1010 2100 1030 2145 L1200 2433 Z" fill="var(--navy-deep)"/>
  <g fill="none" stroke="var(--navy)" stroke-width="2">
    <circle cx="236" cy="1331" r="18"/>
    <path d="M245 1331 H227 M234 1324 L227 1331 L234 1338"/>
    <circle cx="964" cy="1331" r="18"/>
    <path d="M955 1331 H973 M966 1324 L973 1331 L966 1338"/>
  </g>
  <polygon points="358,1265 418,1300 418,1370 358,1405 298,1370 298,1300" fill="#d8d8d8"/>
  <polygon points="358,1276 408,1305 408,1364 358,1393 308,1364 308,1305" fill="var(--white)"/>
  <text x="316" y="1318" font-family="Lato,sans-serif" font-size="14" fill="#888">1</text>
  <text x="358" y="1352" text-anchor="middle" font-family="Lato,sans-serif" font-size="44" fill="var(--navy)">AL</text>
</svg>

<svg class="abs molecule" style="top:52px" viewBox="0 0 44 44" role="img" aria-label="Molekül-Symbol"><polygon points="22,10 32,16 32,28 22,34 12,28 12,16" fill="none" stroke="var(--red)" stroke-width="2"/></svg>
<h1 class="abs center title" style="top:133px">Lassen Sie sich beraten.<br>Kostenlos und unverbindlich.</h1>
<p class="abs lead" style="top:233px">Seit über zehn Jahren forschen wir schwerpunktmäßig an der perfekten Zusammensetzung effektiver Suchmaschinenoptimierung. Als reine SEO Agentur haben wir uns ganz bewusst dafür entschieden, nicht die gesamte Palette des Online Marketings anzubieten, sondern das, wofür unser Herz schlägt und das, was den größten und vor allem nachhaltigsten Erfolg verspricht. Seitdem ist SEO mehr als unser Forschungsgebiet. SEO ist unsere Leidenschaft. Und genau die Liebe zu dem, was wir tun, macht uns so gut, dass wir ausschließlich auf Erfolgsbasis arbeiten.</p>

<h2 class="abs center title" style="top:543px">Jetzt unverbindliche Beratung für Ihe<br>Suchmaschinenoptimierung anfordern</h2>
<div class="field" style="left:217px;top:677px">Vor- und Nachname</div>
<div class="field" style="left:613px;top:677px">Telefonnummer</div>
<div class="field" style="left:217px;top:743px">E-Mail-Adresse</div>
<div class="field" style="left:613px;top:743px">Website</div>
<div class="btn" style="top:846px">Anfrage senden</div>

<h2 class="abs center title" style="top:1084px;line-height:45px">Wir stellen die richtige Verbindung her<br>Schritt für Schritt zur erfolgreichen Webseite</h2>
<h3 class="abs step-title">1. Analyse</h3>
<p class="abs step-text">Bevor wir mit der eigentlichen Optimierung beginnen, nehmen wir uns zunächst die Zeit, um uns ein ausgiebiges Bild vom <b>Ist-Zustand</b> zu verschaffen. Dabei prüfen wir unter anderem mithilfe professioneller <b>SEO-Tools</b>, wie gut Ranking und Sichtbarkeit der vorhandenen Webseite sind, um anschließend gezielte Maßnahmen planen und ergreifen zu können. Wir besprechen gemeinsam mit Ihnen die Analyseergebnisse, erfragen Ihre Vorstellungen sowie Ihre Ziele und beraten Sie <b>kostenlos und unverbindlich</b> zu allen Fragen der Suchmaschinenoptimierung.</p>

<svg class="abs molecule" style="top:1526px" viewBox="0 0 44 44" role="img" aria-label="Molekül-Symbol"><polygon points="22,10 32,16 32,28 22,34 12,28 12,16" fill="none" stroke="var(--red)" stroke-width="2"/></svg>
<h2 class="abs center title" style="top:1614px">Jedes Element trägt zu Ihrem Erfolg bei</h2>
<div class="card" style="left:138px"><h3>Mobile SEO</h3><p>Je nach Branche erfolgt der Großteil der Seitenaufrufe längst über Smartphones und Tablets. Quorix hat deshalb die Mobile-First-Strategie ausgerufen. Nur wer eine für mobile Endgeräte optimierte Webseite hat, kann Spitzenpositionen in den Suchergebnissen belegen. Wir machen Ihre Webseite fit fürs mobile Zeitalter!</p></div>
<div class="card" style="left:455px"><h3>Local SEO</h3><p>50 Prozent der Suchanfragen, die über eine Smartphone getätigt werden, sind lokal. Mit Local SEO beherrschen Sie auch den lokalen Suchindex und können sich über Kunden aus der Umgebung und mit einer deutlich höheren Kaufabsicht freuen – selbst ohne eigene Webseite. Wir zeigen Ihnen, wie das geht!</p></div>
<div class="card" style="left:771px"><h3>Image SEO</h3><p>Multimedialer Content spricht die Besucher nicht nur besser an, er gefällt auch Quorix. Insbesondere Bilder lassen sich gezielt optimieren, um auch über die Quorix Bildersuche Traffic zu generieren. Dabei kommt es vor allem darauf an, der Suchmaschine dabei zu helfen, das Motiv zu interpretieren. Wir erschließen gern neue Trafficquellen für Sie!</p></div>

<h2 class="abs center title" style="top:2056px">Ihre Vorteile auf einen Blick:</h2>
<svg class="tick" style="left:139px;top:2151px" viewBox="0 0 28 28"><circle cx="14" cy="14" r="12.5" fill="none" stroke="var(--red)" stroke-width="1.5"/><path d="M8 14 L12.5 18.5 L20 10" fill="none" stroke="var(--red)" stroke-width="1.5"/></svg>
<svg class="tick" style="left:139px;top:2217px" viewBox="0 0 28 28"><circle cx="14" cy="14" r="12.5" fill="none" stroke="var(--red)" stroke-width="1.5"/><path d="M8 14 L12.5 18.5 L20 10" fill="none" stroke="var(--red)" stroke-width="1.5"/></svg>
<svg class="tick" style="left:139px;top:2283px" viewBox="0 0 28 28"><circle cx="14" cy="14" r="12.5" fill="none" stroke="var(--red)" stroke-width="1.5"/><path d="M8 14 L12.5 18.5 L20 10" fill="none" stroke="var(--red)" stroke-width="1.5"/></svg>
<svg class="tick" style="left:614px;top:2151px" viewBox="0 0 28 28"><circle cx="14" cy="14" r="12.5" fill="none" stroke="var(--red)" stroke-width="1.5"/><path d="M8 14 L12.5 18.5 L20 10" fill="none" stroke="var(--red)" stroke-width="1.5"/></svg>
<svg class="tick" style="left:614px;top:2217px" viewBox="0 0 28 28"><circle cx="14" cy="14" r="12.5" fill="none" stroke="var(--red)" stroke-width="1.5"/><path d="M8 14 L12.5 18.5 L20 10" fill="none" stroke="var(--red)" stroke-width="1.5"/></svg>
<div class="benefit" style="left:191px;top:2142px"><strong>mehr Traffic, mehr Kunden, mehr Umsatz</strong><span>durch höhere Sichtbarkeit und größere Reichweite</span></div>
<div class="benefit" style="left:191px;top:2208px"><strong>Fokus auf erfolgreiches SEO</strong><span>statt alles anzubieten, aber nichts richtig</span></div>
<div class="benefit" style="left:191px;top:2274px"><strong>über 10 Jahre SEO-Erfahrung</strong><span>mit eigenen Webseiten und Projekten von Kunden</span></div>
<div class="benefit" style="left:666px;top:2142px"><strong>100 % erfolgsbasiert</strong><span>erst bezahlen, wenn Sie auf Seite 1 sind</span></div>
<div class="benefit" style="left:666px;top:2208px"><strong>kostenlose Beratung</strong><span>und unverbindliche Angebotserstellung</span></div>

<h2 class="abs center title" style="top:2419px">Fordern Sie jetzt eine kostenlose und<br>unverbindliche Beratung an</h2>
<div class="field" style="left:217px;top:2552px">Vor- und Nachname</div>
<div class="field" style="left:613px;top:2552px">E-Mail-Adresse</div>
<div class="field" style="left:217px;top:2618px">Telefonnummer</div>
<div class="field" style="left:613px;top:2618px">Website</div>
<div class="btn" style="top:2704px">Anfrage senden</div>

<svg class="abs" style="left:590px;top:2770px" width="610" height="272" viewBox="0 0 610 272" role="img" aria-label="Stadtplan mit Standort der Agentur">
  <defs><linearGradient id="mapTone" x1="0" y1="0" x2="1" y2="1"><stop offset="0" stop-color="#ececec"/><stop offset="1" stop-color="#dcdfe3"/></linearGradient></defs>
  <polygon points="213,0 610,90 610,272 0,272" fill="url(#mapTone)"/>
</svg>

<h2 class="abs title" style="left:138px;top:2822px">So erreichen Sie uns</h2>
<div class="abs contact" style="left:138px;top:2874px">Kovalent Studio GmbH<br>Musterstraße 12<br>12345 Musterhausen</div>
<div class="abs contact" style="left:331px;top:2874px">Telefon<br>E-Mail<br>Mo-Fr</div>
<div class="abs contact" style="left:400px;top:2874px">030 555 218 46<br>info@kovalentstudio.de<br>9:00 Uhr - 18:00 Uhr</div>
<div class="abs footer" style="left:138px">© 2018 Kovalent Studio</div>
<div class="abs footer" style="left:312px">Impressum</div>
</body>
</html>
```